Webdesign für Tennisschule
Zielgruppe
Tennisschule für Kinder 4-18 Jahre / Dienstleister im Sportbereich
Aufgabenstellung
Design sollte sich am Corporate Design orientieren. Farblich gerne leuchtende Kontraste, also nicht zu schwach. Das Ganze sollte modern, kompetent und stark wirken. Sprich Farbakzente oder Grafiken am rechten Fleck, eine gute übersichtliche Struktur sollte es geben. Bin kein Fan von einem Mega-Bild auf der Startseite, das wirkt auf mich zu massig.
Es existiert bereits eine 'alte Homepage', diese kann gerne auf Nachfrage eingesehen werden.
Content ist also schon vorhanden, muss aber noch überarbeitet werden.
Da neu gegründet wurde muss jetzt ein neues Design her.

```html
<!DOCTYPE html>
<html lang="de">
<head>
<meta charset="utf-8">
<title>Tennisclub Lindenhain</title>
<link href="https://fonts.googleapis.com/css2?family=Open+Sans:wght@300;400;600;700&display=swap" rel="stylesheet">
<style>
  :root {
    --black: #000000;
    --white: #ffffff;
    --accent: #e04a1b;
    --text-dark: #2b2b2b;
    --text-muted: #8a8a8a;
    --icon: #111111;
  }
  * { box-sizing: border-box; margin: 0; padding: 0; }
  html, body { width: 1200px; height: 590px; overflow: hidden; }
  body {
    font-family: "Open Sans", sans-serif;
    background: var(--white);
    position: relative;
  }
  .topbar {
    position: absolute; left: 0; top: 0; width: 1200px; height: 25px;
    background: var(--black); color: var(--white);
    font-size: 8.8px; font-weight: 400;
  }
  .topbar__contact {
    position: absolute; left: 213px; top: 0; height: 25px;
    display: flex; align-items: center; gap: 13px;
  }
  .topbar__item { display: flex; align-items: center; gap: 4px; }
  .topbar__item svg { width: 8px; height: 8px; }
  .topbar__social {
    position: absolute; right: 218px; top: 7px; display: flex; gap: 8px;
  }
  .topbar__social span {
    width: 11px; height: 11px; background: #d9d9d9; border-radius: 2px;
  }
  .hero {
    position: absolute; left: 0; top: 25px; width: 1200px; height: 319px;
    background: var(--black); overflow: hidden;
  }
  .hero__photo {
    position: absolute; right: 0; top: 0; width: 680px; height: 319px;
    background:
      radial-gradient(ellipse at 85% 30%, #c4441c 0%, #7a2a12 35%, transparent 65%),
      radial-gradient(ellipse at 45% 45%, #4a4a4a 0%, #1c1c1c 45%, transparent 70%),
      linear-gradient(90deg, #000 0%, #151515 35%, #3a1a10 80%, #8a3416 100%);
  }
  .brand {
    position: absolute; left: 213px; top: 30px;
    display: flex; align-items: center; gap: 7px;
  }
  .brand__dot { width: 20px; height: 20px; border-radius: 50%; background: var(--accent); }
  .brand__name { color: var(--white); font-weight: 700; font-size: 14px; letter-spacing: 0.3px; }
  .nav {
    position: absolute; right: 226px; top: 29px;
    display: flex; gap: 25px;
  }
  .nav a {
    color: var(--white); text-decoration: none; font-weight: 700; font-size: 8.8px;
  }
  .hero__title {
    position: absolute; left: 212px; top: 162px;
    color: var(--white); font-weight: 300; font-size: 27px; line-height: 31px;
  }
  .features {
    position: absolute; left: 212px; top: 312px; width: 776px; height: 203px;
    background: var(--white);
    box-shadow: 0 2px 6px rgba(0,0,0,0.18);
  }
  .feature { position: absolute; top: 0; width: 230px; }
  .feature--news { left: 18px; }
  .feature--training { left: 277px; }
  .feature--teams { left: 536px; }
  .feature__icon {
    position: absolute; top: 19px; left: 93px; width: 48px; height: 48px;
    border: 1.3px solid var(--accent); border-radius: 50%;
    display: flex; align-items: center; justify-content: center;
  }
  .feature__icon svg { width: 26px; height: 26px; }
  .feature__title {
    position: absolute; top: 81px; left: 0;
    font-size: 11px; font-weight: 400; letter-spacing: 1.3px; color: var(--text-dark);
  }
  .feature__text {
    position: absolute; top: 110px; left: 0; width: 225px;
    font-size: 10px; line-height: 15.8px; font-weight: 400; color: var(--text-muted);
  }
  .feature__link {
    position: absolute; top: 170px; left: 0;
    font-size: 10px; color: var(--accent); text-decoration: none;
    display: flex; align-items: center; gap: 5px;
  }
  .feature__link svg { width: 7px; height: 7px; }
  .page-edge {
    position: absolute; left: 0; top: 572px; width: 1200px; height: 18px;
    background: linear-gradient(#dcdcdc, #f4f4f4);
  }
</style>
</head>
<body>
  <header class="topbar">
    <div class="topbar__contact">
      <span class="topbar__item">
        <svg viewBox="0 0 10 10"><path d="M5 .8a3 3 0 0 0-3 3c0 2.2 3 5.6 3 5.6s3-3.4 3-5.6a3 3 0 0 0-3-3z" fill="none" stroke="#e04a1b" stroke-width="1"/><circle cx="5" cy="3.8" r="1" fill="#e04a1b"/></svg>
        Ahornweg 12, 10115 Berlin
      </span>
      <span class="topbar__item">
        <svg viewBox="0 0 10 10"><path d="M2 1l2 2-1 1.2c.6 1.2 1.6 2.2 2.8 2.8L7 6l2 2-1.3 1.2C4.5 9 1 5.5.8 2.3z" fill="none" stroke="#e04a1b" stroke-width="0.9"/></svg>
        030 5550172
      </span>
      <span class="topbar__item">
        <svg viewBox="0 0 10 10"><rect x=".8" y="2" width="8.4" height="6.5" rx="1" fill="none" stroke="#e04a1b" stroke-width="0.9"/><path d="M1 2.5l4 3 4-3" fill="none" stroke="#e04a1b" stroke-width="0.9"/></svg>
        info@tc-lindenhain.de
      </span>
    </div>
    <div class="topbar__social"><span></span><span></span><span></span><span></span></div>
  </header>

  <section class="hero">
    <div class="hero__photo" role="img" aria-label="Foto: Tennisspielerin in orangem Sportdress mit Schläger und Ball vor dunklem Hintergrund"></div>
    <div class="brand"><span class="brand__dot"></span><span class="brand__name">Tennisclub Lindenhain</span></div>
    <nav class="nav">
      <a href="#">NEWS</a><a href="#">TRAINING</a><a href="#">TEAM</a><a href="#">KONTAKT</a>
    </nav>
    <h1 class="hero__title">Willkommen bei<br>Berlin's Traditionsverein!</h1>
  </section>

  <section class="features">
    <article class="feature feature--news">
      <div class="feature__icon">
        <svg viewBox="0 0 26 26"><rect x="4" y="5" width="15" height="16" fill="none" stroke="#111" stroke-width="2"/><path d="M19 10h3v9a2 2 0 0 1-4 0" fill="none" stroke="#111" stroke-width="2"/><rect x="7" y="8" width="4" height="4" fill="#111"/><path d="M13 9h4M13 11.5h4M7 15h10M7 17.5h10" stroke="#111" stroke-width="1.4"/></svg>
      </div>
      <h2 class="feature__title">NEWS</h2>
      <p class="feature__text">Lorem ipsum dolor sit amet, consectetur adipiscing elit, sed do eiusmod tempor incididunt ut labore et dolore magna aliqua.</p>
      <a class="feature__link" href="#">Mehr erfahren <svg viewBox="0 0 8 8"><path d="M1 1l3 3-3 3M4 1l3 3-3 3" fill="none" stroke="#222" stroke-width="1.1"/></svg></a>
    </article>
    <article class="feature feature--training">
      <div class="feature__icon">
        <svg viewBox="0 0 26 26">
          <circle cx="10" cy="14" r="6.2" fill="none" stroke="#111" stroke-width="2.6" stroke-dasharray="2.4 2.5"/>
          <circle cx="10" cy="14" r="4.8" fill="#111"/>
          <circle cx="10" cy="14" r="1.8" fill="#fff"/>
          <circle cx="19" cy="7" r="3.6" fill="none" stroke="#111" stroke-width="1.8" stroke-dasharray="1.6 1.2"/>
          <circle cx="19" cy="7" r="2.6" fill="#111"/>
          <circle cx="19" cy="7" r="0.9" fill="#fff"/>
          <circle cx="19" cy="19.5" r="3.6" fill="none" stroke="#111" stroke-width="1.8" stroke-dasharray="1.6 1.2"/>
          <circle cx="19" cy="19.5" r="2.6" fill="#111"/>
          <circle cx="19" cy="19.5" r="0.9" fill="#fff"/>
        </svg>
      </div>
      <h2 class="feature__title">TRAINING</h2>
      <p class="feature__text">Lorem ipsum dolor sit amet, consectetur adipiscing elit, sed do eiusmod tempor incididunt ut labore et dolore magna aliqua.</p>
      <a class="feature__link" href="#">Mehr erfahren <svg viewBox="0 0 8 8"><path d="M1 1l3 3-3 3M4 1l3 3-3 3" fill="none" stroke="#222" stroke-width="1.1"/></svg></a>
    </article>
    <article class="feature feature--teams">
      <div class="feature__icon">
        <svg viewBox="0 0 26 26"><rect x="10.5" y="4" width="5" height="4.5" fill="none" stroke="#111" stroke-width="1.6"/><path d="M13 8.5v3.5M5.5 15v-3h15v3M13 12v3" fill="none" stroke="#111" stroke-width="1.6"/><rect x="3" y="15" width="5" height="4.5" fill="none" stroke="#111" stroke-width="1.6"/><rect x="10.5" y="15" width="5" height="4.5" fill="none" stroke="#111" stroke-width="1.6"/><rect x="18" y="15" width="5" height="4.5" fill="none" stroke="#111" stroke-width="1.6"/></svg>
      </div>
      <h2 class="feature__title">TEAMS</h2>
      <p class="feature__text">Lorem ipsum dolor sit amet, consectetur adipiscing elit, sed do eiusmod tempor incididunt ut labore et dolore magna aliqua.</p>
      <a class="feature__link" href="#">Mehr erfahren <svg viewBox="0 0 8 8"><path d="M1 1l3 3-3 3M4 1l3 3-3 3" fill="none" stroke="#222" stroke-width="1.1"/></svg></a>
    </article>
  </section>

  <div class="page-edge"></div>
</body>
</html>
```